Label design - Superfood blend

We are a family owned nutrition company with big ambitions. Our goal is to develop a range of 100% natural supplements for women, inspired by nature & modern technology that helps them meet their nutritional needs while nourishing them from within. All our products are junk free because we believe that that’s how nature intended it. We also produce products through a sustainable process and only use biodegradable packaging for our products (See link - https://www.pouchwerk.example.uk/biodegradable-stand-pouch-250g-kraft)

Our brand style is modern and minimalist. This same style will be reflected in our social media, website and we want it to be represented through the label designs for our product packaging.

We want some creative designers to design a label that is true to our style (See attached packaging brief with designs we like) and displays our values of Premium, High Quality, Organic Real Food supplements focused on women. I have provided examples in the attached brief, but please only use as inspiration, I dont want any of them to be copied (sorry have had my fingers burnt already !)

Need extra days to review

Hello all, Please note this design is for a LABEL and not the whole package. We will have a 500gm biodegradable brown package, and we will have a label (which is what this project is about) that will be stuck on the front. The size of the label will be a rectangle (unless you come up with a new shape) in the size 20cm * 15cm. Please do not submit designs for the WHOLE from of the package, as we dont intend to have printed packages. Regards

Hello all, I have added a new logo version to the attachments, could you please also try that version. Could you also please look at the new sliders. We are only looking for a minimlaist theme. If you dont know what that means, please do feel free to ask, I would be happy to supply examples. Minimalist designs, means clean, modern, upmarket, elegant designs. It does not use too many colors and mostly sticks to a combination of black and white with colors used sparingly. See some below for your reference anyway. https://www.artbidhub.example.uk/design/48120573 https://www.artbidhub.example.uk/design/52961804 https://www.artbidhub.example.uk/design/47305916 https://www.artbidhub.example.uk/design/46719258 https://www.snapboardly.example.com/search/pins/?q=minimalist%20label%20design&rs=rs&eq=&etslf=2809&term_meta[]=minimalist%7Crecentsearch%7Cundefined&term_meta[]=label%7Crecentsearch%7Cundefined&term_meta[]=design%7Crecentsearch%7Cundefined Regards

Target Market(s)

The target market is women between the age 25 to 45, based in UK (mostly based in larger cities in UK). They are typically middle class or higher and would be in demanding jobs and social lives, that requires for them to meet their nutrition needs in convenient, easy to take forms. The women would also be socially conscious and sensitive to issues like women's rights, environmental issues, healthy food, organic food and sustainability etc. I have a much more detailed customer avatar if required

Font styles to use
Serif
Sans Serif
Decorative
Script

Colors
e8e8e8
474747
1b1b1b
add136

Requirements
Must have
• The label, should look minimalist and modern, throw in some out of the box creativity and we have a winner. Creativity will definitely be of importance. Our packaging is a biodegradable brown paper stand up pouch (Example link in product description). So to make it standout from other colorful packaging - being creative would definitely help.
• Please use the color schemes provided in the brief (See attachments). But if you want to experiment I would be open to it, as long as they are still minimalist and does not stray very far from the color given in the brief :)

```html
<!DOCTYPE html>
<html lang="en">
<head>
<meta charset="utf-8">
<title>Nouravel – Calm Gut Glow label sizes</title>
<link rel="stylesheet" href="https://fonts.googleapis.com/css2?family=Montserrat:wght@300;400;500;600;700;800&display=swap">
<style>
  :root {
    --bg: #e6e6e6;
    --paper: #ffffff;
    --ink: #1b1b1b;
    --rule: #474747;
    --green: #74c27c;
    --dim: #1b1b1b;
  }
  html, body { margin: 0; padding: 0; width: 1200px; height: 1200px; overflow: hidden; background: var(--bg); }
  .sheet { display: block; width: 1200px; height: 1200px; font-family: "Montserrat", Arial, sans-serif; }
  .label-face { fill: var(--paper); }
  .dim-line { stroke: var(--dim); stroke-width: 1.2; fill: none; }
  .dim-text { fill: var(--ink); font-size: 15px; font-weight: 500; }
  .brand { fill: var(--ink); font-weight: 400; }
  .title-main { fill: var(--ink); font-weight: 800; }
  .title-sub { fill: var(--green); font-weight: 700; }
  .subtitle { fill: var(--ink); font-weight: 600; }
  .rule { stroke: var(--rule); stroke-width: 1.2; }
  .ingredient { fill: var(--ink); font-weight: 400; }
  .sep { stroke: var(--ink); stroke-width: 1.4; }
  .category { fill: var(--ink); font-weight: 700; }
  .net { fill: var(--ink); font-weight: 400; }
  .badge { fill: none; stroke: var(--ink); stroke-width: 2.4; }
  .seal { fill: none; stroke: var(--ink); stroke-width: 1.4; }
</style>
</head>
<body>
<svg class="sheet" viewBox="0 0 1400 1400" xmlns="http://www.w3.org/2000/svg">
  <defs>
    <marker id="arrow-head" viewBox="0 0 10 10" refX="9" refY="5" markerWidth="7" markerHeight="7" orient="auto-start-reverse">
      <path d="M0 1 L10 5 L0 9 Z" fill="#1b1b1b"/>
    </marker>
  </defs>
  <rect width="1400" height="1400" fill="var(--bg)"/>

  <!-- Large label dimensions -->
  <g class="dimensions dimensions-large">
    <line class="dim-line" x1="207" y1="330" x2="629" y2="330" marker-start="url(#arrow-head)" marker-end="url(#arrow-head)"/>
    <text class="dim-text" x="418" y="310" text-anchor="middle">150 mm</text>
    <line class="dim-line" x1="168" y1="373" x2="168" y2="936" marker-start="url(#arrow-head)" marker-end="url(#arrow-head)"/>
    <text class="dim-text" x="145" y="667" text-anchor="middle" transform="rotate(-90 145 667)">200 mm</text>
  </g>

  <!-- Large label 150 x 200 mm -->
  <g class="label label-large">
    <rect class="label-face" x="205" y="372" width="425" height="566" rx="14"/>
    <text class="brand" x="290" y="856" font-size="62" textLength="463" lengthAdjust="spacing" transform="rotate(-90 290 856)">NOURAVEL</text>
    <text class="title-main" x="334" y="593" font-size="88" textLength="236" lengthAdjust="spacingAndGlyphs">CALM</text>
    <text class="title-sub" x="339" y="655" font-size="54" textLength="233" lengthAdjust="spacingAndGlyphs">GUT GLOW</text>
    <line class="rule" x1="337" y1="670" x2="590" y2="670"/>
    <text class="subtitle" x="337" y="689" font-size="11" textLength="258" lengthAdjust="spacingAndGlyphs">Organic Prebiotics And Superfood Blend For Women</text>

    <g class="ingredients" font-size="15">
      <text class="ingredient" x="338" y="737" textLength="52" lengthAdjust="spacingAndGlyphs">Baobab</text>
      <line class="sep" x1="405" y1="721" x2="405" y2="739"/>
      <text class="ingredient" x="424" y="737" textLength="60" lengthAdjust="spacingAndGlyphs">Flaxseed</text>
      <line class="rule" x1="337" y1="743" x2="567" y2="743"/>

      <text class="ingredient" x="338" y="764" textLength="70" lengthAdjust="spacingAndGlyphs">Acai Berry</text>
      <line class="sep" x1="428" y1="748" x2="428" y2="766"/>
      <text class="ingredient" x="447" y="764" textLength="93" lengthAdjust="spacingAndGlyphs">Maca Powder</text>
      <line class="rule" x1="337" y1="769" x2="567" y2="769"/>

      <text class="ingredient" x="338" y="790" textLength="67" lengthAdjust="spacingAndGlyphs">Goji Berry</text>
      <line class="sep" x1="422" y1="774" x2="422" y2="792"/>
      <text class="ingredient" x="438" y="790" textLength="85" lengthAdjust="spacingAndGlyphs">Aronia Berry</text>
      <line class="rule" x1="337" y1="795" x2="567" y2="795"/>

      <text class="ingredient" x="338" y="816" textLength="86" lengthAdjust="spacingAndGlyphs">Camu Camu</text>
      <line class="sep" x1="440" y1="800" x2="440" y2="818"/>
      <text class="ingredient" x="454" y="816" textLength="70" lengthAdjust="spacingAndGlyphs">Cinnamon</text>
      <line class="rule" x1="337" y1="821" x2="567" y2="821"/>
    </g>

    <text class="category" x="336" y="855" font-size="13" textLength="135" lengthAdjust="spacingAndGlyphs">FOOD SUPPLEMENT</text>
    <line class="rule" x1="205" y1="875" x2="630" y2="875"/>
    <text class="net" x="267" y="905" font-size="13" text-anchor="middle">Net Weight</text>
    <text class="net" x="267" y="922" font-size="13" text-anchor="middle">500 gm</text>
    <g class="certifications">
      <circle class="badge" cx="363" cy="907" r="16"/>
      <circle class="badge" cx="409" cy="907" r="16"/>
      <circle class="badge" cx="455" cy="907" r="16"/>
      <circle class="seal" cx="504" cy="905" r="20"/>
      <circle class="seal" cx="552" cy="905" r="22"/>
    </g>
  </g>

  <!-- Small label dimensions -->
  <g class="dimensions dimensions-small">
    <line class="dim-line" x1="864" y1="489" x2="1171" y2="489" marker-start="url(#arrow-head)" marker-end="url(#arrow-head)"/>
    <text class="dim-text" x="1020" y="460" text-anchor="middle">110 mm</text>
    <line class="dim-line" x1="828" y1="515" x2="828" y2="936" marker-start="url(#arrow-head)" marker-end="url(#arrow-head)"/>
    <text class="dim-text" x="803" y="735" text-anchor="middle" transform="rotate(-90 803 735)">150 mm</text>
  </g>

  <!-- Small label 110 x 150 mm -->
  <g class="label label-small">
    <rect class="label-face" x="862" y="513" width="311" height="425" rx="12"/>
    <text class="brand" x="925" y="878" font-size="46" textLength="351" lengthAdjust="spacing" transform="rotate(-90 925 878)">NOURAVEL</text>
    <text class="title-main" x="956" y="680" font-size="66" textLength="173" lengthAdjust="spacingAndGlyphs">CALM</text>
    <text class="title-sub" x="960" y="726" font-size="40" textLength="170" lengthAdjust="spacingAndGlyphs">GUT GLOW</text>
    <line class="rule" x1="958" y1="737" x2="1144" y2="737"/>
    <text class="subtitle" x="958" y="751" font-size="8" textLength="190" lengthAdjust="spacingAndGlyphs">Organic Prebiotics And Superfood Blend For Women</text>

    <g class="ingredients" font-size="11">
      <text class="ingredient" x="959" y="788" textLength="38" lengthAdjust="spacingAndGlyphs">Baobab</text>
      <line class="sep" x1="1008" y1="776" x2="1008" y2="790"/>
      <text class="ingredient" x="1022" y="788" textLength="44" lengthAdjust="spacingAndGlyphs">Flaxseed</text>
      <line class="rule" x1="958" y1="792" x2="1127" y2="792"/>

      <text class="ingredient" x="959" y="808" textLength="51" lengthAdjust="spacingAndGlyphs">Acai Berry</text>
      <line class="sep" x1="1024" y1="796" x2="1024" y2="810"/>
      <text class="ingredient" x="1039" y="808" textLength="68" lengthAdjust="spacingAndGlyphs">Maca Powder</text>
      <line class="rule" x1="958" y1="812" x2="1127" y2="812"/>

      <text class="ingredient" x="959" y="827" textLength="49" lengthAdjust="spacingAndGlyphs">Goji Berry</text>
      <line class="sep" x1="1020" y1="815" x2="1020" y2="829"/>
      <text class="ingredient" x="1032" y="827" textLength="63" lengthAdjust="spacingAndGlyphs">Aronia Berry</text>
      <line class="rule" x1="958" y1="831" x2="1127" y2="831"/>

      <text class="ingredient" x="959" y="847" textLength="63" lengthAdjust="spacingAndGlyphs">Camu Camu</text>
      <line class="sep" x1="1033" y1="835" x2="1033" y2="849"/>
      <text class="ingredient" x="1044" y="847" textLength="52" lengthAdjust="spacingAndGlyphs">Cinnamon</text>
      <line class="rule" x1="958" y1="851" x2="1127" y2="851"/>
    </g>

    <text class="category" x="958" y="876" font-size="10" textLength="99" lengthAdjust="spacingAndGlyphs">FOOD SUPPLEMENT</text>
    <line class="rule" x1="862" y1="891" x2="1173" y2="891"/>
    <text class="net" x="907" y="913" font-size="10" text-anchor="middle">Net Weight</text>
    <text class="net" x="907" y="926" font-size="10" text-anchor="middle">300 gm</text>
    <g class="certifications">
      <circle class="badge" cx="977" cy="915" r="12"/>
      <circle class="badge" cx="1011" cy="915" r="12"/>
      <circle class="badge" cx="1045" cy="915" r="12"/>
      <circle class="seal" cx="1081" cy="914" r="15"/>
      <circle class="seal" cx="1114" cy="913" r="16"/>
    </g>
  </g>
</svg>
</body>
</html>
```